Business card for my new company (Accounting firm)

I need a business card for my new business Corvane Advisory and Ledger SA. Our services are accounting, tax, audit and financial management. Our customers are small companies, start-ups and new companies. The final design has to show financial security, trust and growth. Please find our logo attached to the business card. Text for the business card: Corvane Advisory and Ledger SA Tomas da Varela Director and Founder Certified Accountant Tel. 022 418 27 35 tv@corvaneconseil.ch www.corvaneconseil.ch Rue des Vergers-Bleus 14 1201 Geneva
Target Market(s)
Our customers are small companies, start-ups and new companies.
Industry/Entity Type
Finance And Accounting
Contact Information for Business Card
Corvane Conseil et Registre SA
Tomas da Varela
Directeur et Fondateur
Expert-comptable diplômé
Tél. 022 418 27 35
tv@corvaneconseil.ch
www.corvaneconseil.ch
Rue des Vergers-Bleus 14
1201 Genève

```html
<!DOCTYPE html>
<html lang="en">
<head>
<meta charset="utf-8">
<title>Corvane Conseil et Registre SA – Business Card</title>
<link rel="stylesheet" href="https://fonts.googleapis.com/css2?family=Lato:wght@400;700&display=swap">
<style>
  :root {
    --backdrop: #9c9c9c;
    --card-white: #ffffff;
    --card-charcoal: #3c3c3e;
    --blue-light: #2eaee2;
    --blue-mid: #1e8ac8;
    --blue-deep: #166596;
    --ink: #474747;
    --white: #ffffff;
  }
  * { box-sizing: border-box; margin: 0; padding: 0; }
  html, body { width: 1200px; height: 802px; overflow: hidden; }
  body {
    background: var(--backdrop);
    position: relative;
    font-family: "Lato", sans-serif;
  }
  .card {
    position: absolute;
    top: 274px;
    width: 443px;
    height: 264px;
    overflow: hidden;
  }
  .card--front { left: 136px; background: var(--card-white); }
  .card--back { left: 624px; background: var(--card-charcoal); }

  .holder { position: absolute; left: 23px; top: 36px; }
  .holder__name {
    color: var(--blue-light);
    font-weight: 700;
    font-size: 15.5px;
    letter-spacing: -0.2px;
    line-height: 17px;
  }
  .holder__role {
    color: var(--ink);
    font-size: 12.5px;
    line-height: 15.5px;
  }

  .contact { position: absolute; left: 23px; top: 108px; list-style: none; }
  .contact__item {
    display: flex;
    align-items: center;
    gap: 10px;
    color: var(--ink);
    font-size: 12.5px;
    line-height: 16px;
  }
  .contact__icon { width: 11px; height: 11px; flex: none; fill: var(--blue-mid); }

  .address {
    position: absolute;
    left: 23px;
    top: 170px;
    color: var(--ink);
    font-size: 12.5px;
    line-height: 15.5px;
    font-style: normal;
  }

  .front-brand {
    position: absolute;
    right: 22px;
    top: 28px;
    bottom: 22px;
    display: flex;
    flex-direction: column;
    align-items: flex-end;
    justify-content: space-between;
  }
  .front-brand__mark {
    width: 56px;
    height: 56px;
    background: var(--blue-deep);
  }
  .front-brand__name {
    color: var(--blue-mid);
    font-weight: 700;
    font-size: 56px;
    line-height: 1;
    letter-spacing: 0.5px;
  }

  .back-brand {
    position: absolute;
    left: 0; right: 0;
    top: 62px;
    display: flex;
    flex-direction: column;
    align-items: center;
  }
  .back-brand__mark {
    width: 52px;
    height: 52px;
    background: var(--blue-mid);
    margin-bottom: 40px;
  }
  .back-brand__name {
    color: var(--white);
    font-weight: 400;
    font-size: 34px;
    line-height: 1;
    letter-spacing: 2px;
  }
  .back-brand__line {
    margin-top: 6px;
    color: var(--white);
    font-weight: 400;
    font-size: 10.5px;
    letter-spacing: 2px;
    text-transform: uppercase;
  }
</style>
</head>
<body>
  <section class="card card--front" aria-label="Business card front">
    <div class="holder">
      <p class="holder__name">TOMAS DA VARELA</p>
      <p class="holder__role">Director and Founder</p>
      <p class="holder__role">Certified Accountant</p>
    </div>

    <ul class="contact">
      <li class="contact__item">
        <svg class="contact__icon" viewBox="0 0 12 12" aria-hidden="true">
          <path d="M1 4.2C1 2.5 3.2 1.5 6 1.5s5 1 5 2.7V5H8.5V3.8h-5V5H1z"/>
          <rect x="2.5" y="5.5" width="7" height="5" rx="1"/>
        </svg>
        <span>022 418 27 35</span>
      </li>
      <li class="contact__item">
        <svg class="contact__icon" viewBox="0 0 12 12" aria-hidden="true">
          <path d="M1 2.5h10v7H1z M1.6 3.1 6 6.6l4.4-3.5" fill="none" stroke="#1e8ac8" stroke-width="1.2"/>
        </svg>
        <span>tv@corvaneconseil.ch</span>
      </li>
      <li class="contact__item">
        <svg class="contact__icon" viewBox="0 0 12 12" aria-hidden="true">
          <circle cx="6" cy="6" r="5"/>
          <path d="M4 3.5c1 .5 1 1.5.3 2.3.8.6 1.6.3 2 1.3-.5 1 .3 1.7.2 2.5M8.3 3c-.5.8 0 1.6.8 1.8" fill="none" stroke="#fff" stroke-width=".9"/>
        </svg>
        <span>www.corvaneconseil.ch</span>
      </li>
    </ul>

    <address class="address">
      Rue des Vergers-Bleus 14<br>
      1201 Geneva
    </address>

    <div class="front-brand">
      <span class="front-brand__mark"></span>
      <p class="front-brand__name">Corvane</p>
    </div>
  </section>

  <section class="card card--back" aria-label="Business card back">
    <div class="back-brand">
      <span class="back-brand__mark"></span>
      <p class="back-brand__name">CORVANE</p>
      <p class="back-brand__line">Conseil et Registre</p>
    </div>
  </section>
</body>
</html>
```